Poster to advertise that we repair vexo, brev, dorvane phone and tablets

We are a computer repair business and we also repair Vexo, Brev and Dorvane phone / tablets.

This poster is required to go onto the wall of a shop frequented by students and to inform them that we now repair the above.

The poster does not need any shop details, no phone numbers or prices, it just needs to state we repair :-

Vexos
Brevs
Dorvane Phones
Dorvane Tablets

Also the bias for repairs should be slanted towards screen repairs rather than any other type of repair.

Another claim can be that all repairs are usually by the next day and the best price is guaranteed.

We have the following websites for more info :-

www.brackledesk.co.uk
www.brackleslate.co.uk

```html
<!DOCTYPE html>
<html lang="en">
<head>
<meta charset="utf-8">
<title>Next Day Repair Poster</title>
<link href="https://fonts.googleapis.com/css2?family=Archivo:wght@500;700;800;900&family=Archivo+Black&display=swap" rel="stylesheet">
<style>
  :root {
    --bg-top: #c7cfd8;
    --bg-bottom: #e4e7eb;
    --ink: #1c1f24;
    --device-edge: #2a2e34;
    --device-body: #14171b;
    --screen-dark: #050607;
    --glow: #86dcf0;
  }
  * { margin: 0; padding: 0; box-sizing: border-box; }
  html, body { width: 809px; height: 1200px; overflow: hidden; }
  body {
    background: linear-gradient(180deg, var(--bg-top) 0%, var(--bg-bottom) 100%);
    font-family: "Archivo", Arial, sans-serif;
    color: var(--ink);
  }
  .poster { position: relative; width: 809px; height: 1200px; }

  .tagline {
    position: absolute; top: 72px; left: 0; width: 100%;
    text-align: center; font-size: 23px; font-weight: 500;
    letter-spacing: 3.5px; text-transform: uppercase;
  }
  .tagline strong { font-weight: 900; font-size: 25px; }

  .device-photo {
    position: absolute; left: 185px; top: 145px; width: 425px; height: 870px;
    border-radius: 58px;
    background: linear-gradient(160deg, var(--device-edge) 0%, var(--device-body) 45%, var(--screen-dark) 100%);
  }

  .headline {
    position: absolute; left: 222px; top: 318px; width: 376px;
    text-align: center; font-family: "Archivo Black", Arial, sans-serif;
    color: var(--glow); font-size: 84px; line-height: 106px;
    letter-spacing: -1px; text-transform: uppercase;
  }

  .services {
    position: absolute; top: 1072px; left: 0; width: 100%; text-align: center;
  }
  .services-title { font-size: 27px; font-weight: 800; letter-spacing: 0.2px; line-height: 30px; }
  .services-list { font-size: 16.5px; font-weight: 700; line-height: 22px; }
</style>
</head>
<body>
  <main class="poster">
    <p class="tagline">The <strong>Best Price</strong> is guaranteed</p>

    <div class="device-photo" role="img" aria-label="Smartphone with a cracked glass screen"></div>

    <h1 class="headline">Next<br>Day<br>Repair</h1>

    <section class="services">
      <h2 class="services-title">WE REPAIR ALL</h2>
      <p class="services-list">Vexos, Brevs, Dorvane Phones and Dorvane Tablets</p>
    </section>
  </main>
</body>
</html>
```